HarmoNest Ensemble Jubilee
Date: Sunday Oct 2, 2022
When: 2-4 p.m.
Location: Brindle9 Alehouse
413 Marlowe Ct #200, Sacramento, CA 95821
Tickets: www.Tixolvo.com
General seating: $15 for adults and $10 for students

```html
<!DOCTYPE html>
<html lang="en">
<head>
<meta charset="utf-8">
<title>HarmoNest Ensemble Jubilee</title>
<link rel="stylesheet" href="https://fonts.googleapis.com/css2?family=Bebas+Neue&family=Montserrat:wght@500;600;700;800&display=swap">
<style>
  :root {
    --stage: #4a4a4a;
    --peach: #f6a98c;
    --peach-soft: #fbd9cc;
    --lavender: #e9d3f2;
    --navy: #33318a;
    --venue: #35307f;
    --ink: #151515;
    --paper: #ffffff;
  }
  * { margin: 0; padding: 0; box-sizing: border-box; }
  html, body { width: 1200px; height: 1200px; overflow: hidden; background: var(--stage); }
  .poster {
    position: absolute; left: 172px; top: 45px; width: 856px; height: 1109px;
    overflow: hidden;
    background:
      radial-gradient(ellipse 55% 40% at 10% 85%, rgba(196,55,201,.85), transparent 70%),
      radial-gradient(ellipse 50% 35% at 20% 65%, rgba(236,127,201,.85), transparent 70%),
      radial-gradient(ellipse 40% 25% at 5% 100%, rgba(141,95,224,.6), transparent 70%),
      radial-gradient(ellipse 70% 50% at 75% 25%, var(--peach), transparent 75%),
      linear-gradient(180deg, var(--peach-soft), #f8c9d8 60%, var(--lavender));
    font-family: "Montserrat", sans-serif;
    color: var(--ink);
  }
  .poster > * { position: absolute; line-height: 1; white-space: nowrap; }
  .backdrop { left: 0; top: 0; }
  .title { left: 46px; font-family: "Bebas Neue", sans-serif; font-weight: 400; -webkit-background-clip: text; background-clip: text; color: transparent; }
  .title--one { top: 23px; font-size: 162px; background-image: linear-gradient(90deg, #d950c9, #f08a7a); }
  .title--two { top: 167px; font-size: 162px; background-image: linear-gradient(90deg, #c983e4, #5a3de0); }
  .title--three { top: 323px; font-size: 117px; background-image: linear-gradient(90deg, var(--navy) 45%, #d040d0); }
  .venue { left: 46px; top: 452px; font-size: 31px; font-weight: 700; color: var(--venue); }
  .day { left: 44px; top: 556px; font-size: 88px; font-weight: 600; }
  .date { left: 44px; top: 650px; font-size: 62px; font-weight: 600; }
  .info { left: 46px; display: flex; align-items: center; gap: 8px; }
  .info svg { flex: none; }
  .info--time { top: 728px; font-size: 30px; font-weight: 600; }
  .info--place { top: 775px; font-size: 21px; font-weight: 500; }
  .info .sep { display: inline-block; width: 2px; height: 22px; background: var(--ink); }
  .tickets { left: 46px; top: 826px; font-size: 33px; font-weight: 800; }
  .tickets-arrow { left: 194px; top: 820px; }
  .url { left: 46px; top: 874px; font-size: 33px; font-weight: 800; }
  .rule { left: 42px; top: 921px; width: 388px; height: 2px; background: var(--ink); }
  .seating-label { left: 46px; top: 949px; font-size: 21px; font-weight: 500; }
  .price { left: 44px; font-size: 41px; font-weight: 600; }
  .price--adult { top: 982px; }
  .price--student { top: 1032px; }
</style>
</head>
<body>
<main class="poster">
  <svg class="backdrop" width="856" height="1109" viewBox="0 0 856 1109">
    <defs>
      <linearGradient id="paperFade" x1="0" y1="0" x2="1" y2="0">
        <stop offset="0" stop-color="#ffffff"/>
        <stop offset=".55" stop-color="#fff8f6" stop-opacity=".95"/>
        <stop offset="1" stop-color="#fde5dc" stop-opacity="0"/>
      </linearGradient>
      <linearGradient id="instruments" x1="0" y1="0" x2="0" y2="1">
        <stop offset="0" stop-color="#f3d9dc"/>
        <stop offset=".35" stop-color="#c974a8"/>
        <stop offset=".6" stop-color="#e0b56a"/>
        <stop offset="1" stop-color="#d99a2e"/>
      </linearGradient>
    </defs>
    <path class="paper-wave" d="M0 0 H700 V480 C560 500 460 560 330 545 C200 530 90 500 0 495 Z" fill="url(#paperFade)"/>
    <path class="instruments-art" role="img" aria-label="Watercolour illustration of a winding piano keyboard, double bass, saxophone and trumpet with musical notes"
      d="M856 40 C760 40 700 70 650 120 C720 220 760 330 700 430 C600 450 440 470 420 560 C410 700 480 830 560 900 C600 960 640 1010 650 1109 H856 Z"
      fill="url(#instruments)" opacity=".8"/>
  </svg>

  <h1 class="title title--one">HARMONEST</h1>
  <h1 class="title title--two">ENSEMBLE</h1>
  <h1 class="title title--three">JUBILEE</h1>

  <p class="venue">Brindle9 Alehouse</p>

  <p class="day">Sunday</p>
  <p class="date">Oct 2, 2022</p>

  <p class="info info--time">
    <svg width="26" height="24" viewBox="0 0 26 24" aria-hidden="true">
      <rect x="1" y="3" width="19" height="17" rx="2" fill="none" stroke="#151515" stroke-width="2"/>
      <line x1="1" y1="8" x2="20" y2="8" stroke="#151515" stroke-width="2"/>
      <circle cx="19" cy="18" r="5" fill="#fff" stroke="#151515" stroke-width="2"/>
      <path d="M19 15.5 V18 H21" fill="none" stroke="#151515" stroke-width="1.5"/>
    </svg>
    <span class="sep"></span>2-4 p.m.
  </p>
  <p class="info info--place">
    <svg width="16" height="20" viewBox="0 0 16 20" aria-hidden="true">
      <path d="M8 1 C4 1 1 4 1 8 C1 13 8 19 8 19 C8 19 15 13 15 8 C15 4 12 1 8 1 Z" fill="#151515"/>
      <circle cx="8" cy="8" r="2.6" fill="#fff"/>
    </svg>
    <span class="sep"></span>413 Marlowe Ct #200, Sacramento, CA 95821
  </p>

  <p class="tickets">Tickets:</p>
  <svg class="tickets-arrow" width="80" height="46" viewBox="0 0 80 46" aria-hidden="true">
    <path d="M4 20 C20 2 52 0 68 34" fill="none" stroke="#151515" stroke-width="3.5" stroke-linecap="round"/>
    <path d="M58 30 L69 38 L74 24" fill="none" stroke="#151515" stroke-width="3.5" stroke-linecap="round" stroke-linejoin="round"/>
  </svg>
  <p class="url">www.Tixolvo.com</p>
  <div class="rule"></div>

  <p class="seating-label">General seating:</p>
  <p class="price price--adult">$15 for adults and</p>
  <p class="price price--student">$10 for students</p>
</main>
</body>
</html>
```